" A Pravelo atua no setor de mobilidade elétrica, oferecendo soluções completas de recarga para veículos elétricos. Nossa empresa instala e gerencia pontos de recarga inteligentes conectados ao nosso sistema próprio (SCMS), que permite o controle, monitoramento e faturamento das recargas em tempo real. Além disso, oferecemos um aplicativo intuitivo para motoristas e opções de white label para parceiros que desejam operar seus próprios pontos de recarga. "

```html
<!DOCTYPE html>
<html lang="pt-BR">
<head>
<meta charset="utf-8">
<title>Pravelo – Como recarregar</title>
<link href="https://fonts.googleapis.com/css2?family=Baloo+2:wght@500;600;700&display=swap" rel="stylesheet">
<style>
  :root{
    --bg:#6e6e6e;
    --paper:#f5f6f5;
    --green:#4cbb5a;
    --green-dark:#2f9a44;
    --green-light:#7fd68a;
    --green-soft:rgba(76,187,90,.22);
    --ink:#333b36;
    --white:#ffffff;
    --device:#1d2a3a;
  }
  *{margin:0;padding:0;box-sizing:border-box}
  html,body{width:1200px;height:1200px;overflow:hidden;background:var(--bg)}
  body{font-family:"Baloo 2",sans-serif;color:var(--ink)}
  .flyer{position:absolute;left:84px;top:0;width:1032px;height:1135px;background:var(--paper);overflow:hidden}

  .decor-area{position:absolute;background:radial-gradient(ellipse at center,var(--green-soft),rgba(76,187,90,0) 70%)}
  .decor-top-right{left:760px;top:0;width:272px;height:470px}
  .decor-left{left:-60px;top:380px;width:160px;height:260px}
  .decor-right{left:900px;top:500px;width:120px;height:140px}

  .step{position:absolute;left:127px;display:flex;align-items:flex-start;gap:32px}
  .step-number{width:140px;height:144px;border-radius:24px;background:linear-gradient(160deg,var(--green-light),var(--green-dark));
    color:var(--white);font-weight:700;font-size:70px;display:flex;align-items:center;justify-content:center;
    box-shadow:0 6px 12px rgba(0,0,0,.18)}
  .step-text{font-weight:600;font-size:41px;line-height:46px;padding-top:0}
  .step-3{top:19px}.step-4{top:211px}.step-5{top:403px}

  .install{position:absolute;left:122px;top:672px;font-weight:600;font-size:45px;line-height:54px}

  .support-band{position:absolute;left:74px;top:857px;width:562px;height:103px;background:var(--green);
    border-radius:0 52px 52px 0;display:flex;align-items:center;gap:30px;padding-left:42px;color:var(--white);
    font-weight:600;font-size:33px;line-height:36px}
  .support-band svg{flex:none}

  .contact{position:absolute;left:113px;display:flex;align-items:center;gap:14px;font-weight:500;font-size:36px}
  .contact-phone{top:983px}.contact-mail{top:1033px}

  .device{position:absolute;left:641px;top:641px;width:312px;height:520px;border-radius:52px;background:var(--device);padding:14px}
  .device-screen{width:100%;height:100%;border-radius:40px;background:linear-gradient(170deg,var(--green-light),var(--green-dark));
    display:flex;align-items:center;justify-content:center;color:var(--white);font-weight:700;font-size:52px}
</style>
</head>
<body>
<main class="flyer">
  <div class="decor-area decor-top-right" role="img" aria-label="Área decorativa verde da marca"></div>
  <div class="decor-area decor-left" role="img" aria-label="Área decorativa com folha verde"></div>
  <div class="decor-area decor-right" role="img" aria-label="Área decorativa com folha verde"></div>

  <div class="step step-3"><div class="step-number">03</div><p class="step-text">Informe seu nome<br>e e-mail para<br>continuar.</p></div>
  <div class="step step-4"><div class="step-number">04</div><p class="step-text">Cadastre um cartão<br>de crédito ou adicione<br>saldo à carteira via Pix.</p></div>
  <div class="step step-5"><div class="step-number">05</div><p class="step-text">Toque em “Iniciar<br>recarga” e acompanhe<br>o processo pelo celular.</p></div>

  <p class="install">Para maior comodidade,<br>instale o aplicativo<br>no seu dispositivo.</p>

  <div class="support-band">
    <svg width="46" height="46" viewBox="0 0 24 24" fill="none" stroke="currentColor" stroke-width="2" stroke-linecap="round">
      <path d="M4 14v-2a8 8 0 0 1 16 0v2"/><rect x="3" y="13" width="4" height="6" rx="1.5" fill="currentColor"/><rect x="17" y="13" width="4" height="6" rx="1.5" fill="currentColor"/><path d="M19 19c0 2-2 3-5 3"/>
    </svg>
    <span>Suporte técnico em tempo<br>real, críticas ou sugestões.</span>
  </div>

  <div class="contact contact-phone">
    <svg width="36" height="36" viewBox="0 0 24 24" fill="none" stroke="var(--green-dark)" stroke-width="2"><circle cx="12" cy="12" r="9.5"/><path d="M9 7.5c-1 .5-1.5 1.8-.5 3.8s3 3.7 4.5 4.2 2.5-.2 3-1l-1.8-1.3-1 .8c-1-.4-2.3-1.6-2.8-2.7l.8-1L10 8z" fill="var(--green-dark)" stroke="none"/></svg>
    <span>(11) 98765-4321</span>
  </div>
  <div class="contact contact-mail">
    <svg width="40" height="30" viewBox="0 0 26 18" fill="none" stroke="var(--green-dark)" stroke-width="1.8"><rect x="1" y="1" width="24" height="16" rx="1.5"/><path d="M1 2l12 9 12-9"/></svg>
    <span>suporte@pravelo.com.br</span>
  </div>

  <div class="device" role="img" aria-label="Smartphone exibindo o aplicativo Pravelo">
    <div class="device-screen">Pravelo</div>
  </div>
</main>
</body>
</html>
```